Ostrel Appraisals BV business cards (a financial services company)

I am looking for a business card design that stands out in the financial advisory field of business & intellectual property valuation. The business card design should be conservative, yet different. Address details have changed since the attached business card. New address is:

Molenvlietkade 27
4817 KT Leiden
The Netherlands

Telephone number remains the same.

```html
<!DOCTYPE html>
<html lang="en">
<head>
<meta charset="utf-8">
<title>Ostrel Appraisals BV – Business Cards</title>
<link href="https://fonts.googleapis.com/css2?family=Josefin+Sans:wght@300;400&family=Nunito+Sans:wght@300;400;600&display=swap" rel="stylesheet">
<style>
  :root {
    --backdrop: #2a2a2d;
    --card: #1d1f21;
    --silver: #9c9fa3;
    --silver-soft: #7d8084;
    --white: #eceeef;
    --rule: #55585c;
  }
  * { box-sizing: border-box; margin: 0; padding: 0; }
  html, body { width: 1200px; height: 800px; overflow: hidden; }
  body {
    background: var(--backdrop);
    font-family: "Nunito Sans", sans-serif;
    position: relative;
  }
  .card {
    position: absolute;
    top: 250px;
    width: 520px;
    height: 300px;
    background: var(--card);
    border-radius: 18px;
    box-shadow: 0 18px 40px rgba(0,0,0,.45);
    overflow: hidden;
  }
  .card--front { left: 45px; }
  .card--back  { left: 635px; }

  /* Front */
  .front-brand {
    position: absolute;
    left: 0; right: 0; top: 108px;
    display: flex;
    justify-content: center;
    align-items: center;
    gap: 14px;
  }
  .brand-mark {
    width: 14px; height: 14px;
    background: var(--silver);
  }
  .brand-name {
    font-family: "Josefin Sans", sans-serif;
    font-weight: 300;
    font-size: 30px;
    letter-spacing: 2px;
    color: var(--silver);
    text-transform: uppercase;
    white-space: nowrap;
  }
  .front-web {
    position: absolute;
    left: 0; right: 0; top: 180px;
    text-align: center;
    font-size: 12px;
    letter-spacing: 5px;
    color: var(--silver-soft);
    text-transform: uppercase;
  }

  /* Back */
  .person {
    position: absolute;
    left: 40px; top: 30px;
  }
  .person-name {
    font-size: 20px;
    font-weight: 400;
    letter-spacing: 1.2px;
    line-height: 1.2;
    color: var(--silver-soft);
    text-transform: uppercase;
    white-space: nowrap;
  }
  .person-role {
    font-size: 16px;
    font-weight: 600;
    line-height: 1.3;
    color: var(--white);
    margin-top: 2px;
    white-space: nowrap;
  }
  .back-brand {
    position: absolute;
    left: 40px; top: 118px;
    width: 96px;
    font-family: "Josefin Sans", sans-serif;
    font-weight: 300;
    font-size: 13px;
    line-height: 1.35;
    letter-spacing: 1px;
    color: var(--silver);
    text-transform: uppercase;
  }
  .divider {
    position: absolute;
    left: 148px; top: 110px;
    width: 1px; height: 112px;
    background: var(--rule);
  }
  .contacts {
    position: absolute;
    left: 164px; top: 108px;
    list-style: none;
    font-size: 12.5px;
    color: var(--silver-soft);
  }
  .contacts li {
    display: flex;
    align-items: center;
    gap: 9px;
    height: 21px;
    white-space: nowrap;
  }
  .contacts svg { width: 12px; height: 12px; fill: var(--white); flex: none; }
  .address {
    position: absolute;
    left: 164px; top: 182px;
    font-size: 13px;
    font-style: normal;
    line-height: 1.45;
    color: var(--silver-soft);
    white-space: nowrap;
  }
  .tagline {
    position: absolute;
    left: 40px; right: 30px; bottom: 28px;
    font-size: 13px;
    letter-spacing: 0.6px;
    color: var(--white);
    text-transform: uppercase;
    white-space: nowrap;
  }
</style>
</head>
<body>

  <section class="card card--front" aria-label="Card front">
    <div class="front-brand">
      <span class="brand-mark"></span>
      <span class="brand-name">Ostrel Appraisals</span>
    </div>
    <p class="front-web">www.ostrelappraisals.com</p>
  </section>

  <section class="card card--back" aria-label="Card back">
    <div class="person">
      <h1 class="person-name">Maarten Velde, CFA, ASA, RV</h1>
      <p class="person-role">Managing Director</p>
    </div>

    <div class="back-brand">Ostrel Appraisals</div>
    <div class="divider"></div>

    <ul class="contacts">
      <li>
        <svg viewBox="0 0 24 24" aria-hidden="true"><path d="M6.6 10.8a15.1 15.1 0 0 0 6.6 6.6l2.2-2.2a1 1 0 0 1 1-.25 11.4 11.4 0 0 0 3.6.57 1 1 0 0 1 1 1V20a1 1 0 0 1-1 1A17 17 0 0 1 3 4a1 1 0 0 1 1-1h3.5a1 1 0 0 1 1 1c0 1.25.2 2.45.57 3.57a1 1 0 0 1-.25 1z"/></svg>
        +31 (0)70 480 1936
      </li>
      <li>
        <svg viewBox="0 0 24 24" aria-hidden="true"><path d="M2 5h20v14H2z M3.5 6.5 12 13l8.5-6.5" stroke="#1d1f21" stroke-width="1.6"/></svg>
        mvelde@ostrelappraisals.com
      </li>
      <li>
        <svg viewBox="0 0 24 24" aria-hidden="true"><circle cx="12" cy="12" r="10"/><path d="M2 12h20M12 2c3 3 3 17 0 20M12 2c-3 3-3 17 0 20" stroke="#1d1f21" stroke-width="1.4" fill="none"/></svg>
        www.ostrelappraisals.com
      </li>
    </ul>

    <address class="address">
      Molenvlietkade 27<br>
      4817 KT Leiden, The Netherlands
    </address>

    <p class="tagline">Business and Intellectual Property Valuations</p>
  </section>

</body>
</html>
```